ORBIT conference Slide Deck

This is a conference for our team that will be 3 days of discussions on how to build our business in the middle of these challenging time. Its a bit of a battle and so we are going with a red and grey/black these although I am open to your interpretation. I will include a few graphics that we have started on to show you the look. But I am just getting started, INSPIRE ME! The screen will be 100' across the front of the room and these decks will show on each side and I will reformat for the middle 1X6 screen as needed. I have the AI file of the logo if you need it. I don't see where to upload it here.

Target Market(s)

our top producers

Industry/Entity Type

Real Estate Agent

Font styles to use
Sans Serif

Colors
ec1f27

Requirements
Must have
• Depth, creativity

```html
<!DOCTYPE html>
<html lang="en">
<head>
<meta charset="UTF-8">
<title>ORBIT Conference Slide</title>
<link href="https://fonts.googleapis.com/css2?family=Montserrat:wght@400;700;800&display=swap" rel="stylesheet">
<style>
  :root {
    --red: #ec1f27;
    --black: #000000;
    --paper: #f3f3f3;
    --ink: #222222;
    --white: #ffffff;
  }
  * { margin: 0; padding: 0; box-sizing: border-box; }
  html, body { width: 1200px; height: 675px; overflow: hidden; background: var(--paper); }
  .slide {
    position: relative;
    width: 1200px;
    height: 675px;
    overflow: hidden;
    font-family: "Montserrat", sans-serif;
  }
  .backdrop { position: absolute; inset: 0; }
  .title {
    position: absolute;
    left: 101px;
    top: 172px;
    color: var(--white);
    font-weight: 800;
    font-size: 40px;
    line-height: 46px;
    letter-spacing: 0.13em;
    white-space: nowrap;
  }
  .headline {
    position: absolute;
    left: 560px;
    width: 325px;
    top: 170px;
    color: var(--ink);
    font-weight: 700;
    font-size: 25.5px;
    line-height: 34px;
    text-align: center;
    white-space: nowrap;
  }
  .body-copy {
    position: absolute;
    top: 374px;
    left: 0;
    color: var(--ink);
    font-weight: 400;
    font-size: 18.5px;
    line-height: 26.2px;
  }
  .body-copy .line {
    position: relative;
    display: block;
    width: 328px;
    text-align: justify;
    text-align-last: justify;
    white-space: nowrap;
  }
  .body-copy .line.last { text-align-last: left; }
  .caption {
    position: absolute;
    left: 893px;
    top: 164px;
    width: 232px;
    height: 55px;
    display: flex;
    align-items: center;
    justify-content: center;
    color: var(--white);
    font-weight: 700;
    font-size: 24px;
    letter-spacing: 0.1em;
  }
  .brand {
    position: absolute;
    left: 1030px;
    top: 596px;
    color: var(--red);
    font-weight: 800;
    font-size: 44px;
    line-height: 46px;
    letter-spacing: 0.04em;
  }
</style>
</head>
<body>
<main class="slide">
  <svg class="backdrop" viewBox="0 0 1200 675" width="1200" height="675" aria-hidden="false">
    <defs>
      <linearGradient id="skyline-tones" x1="0" y1="0" x2="0" y2="1">
        <stop offset="0" stop-color="#b9c9de"/>
        <stop offset="0.45" stop-color="#c9b59a"/>
        <stop offset="1" stop-color="#6b5a48"/>
      </linearGradient>
      <linearGradient id="city-tones" x1="0" y1="0" x2="0" y2="1">
        <stop offset="0" stop-color="#9db3da"/>
        <stop offset="0.5" stop-color="#a89277"/>
        <stop offset="0.85" stop-color="#5b5a55"/>
        <stop offset="1" stop-color="#2f5c8f"/>
      </linearGradient>
    </defs>

    <!-- left dark panel -->
    <polygon class="panel-dark" points="0,0 526,0 463,675 0,675" fill="var(--black)"/>
    <!-- right dark panel -->
    <polygon class="panel-dark" points="1055,0 1200,0 1200,675 988,675" fill="var(--black)"/>
    <!-- red divider stripe -->
    <polygon class="divider" points="1043,0 1055,0 988,675 976,675" fill="var(--red)"/>

    <!-- title frame bracket -->
    <g class="title-frame" fill="var(--red)">
      <rect x="73" y="154" width="120" height="7"/>
      <rect x="73" y="154" width="7" height="132"/>
      <rect x="73" y="279" width="115" height="7"/>
      <polygon points="182,265 189,265 186,286 179,286"/>
    </g>

    <!-- skyline photo area, lower left -->
    <polygon points="75,425 438,425 418,675 75,675" fill="url(#skyline-tones)"
             role="img" aria-label="Photo of residential high-rise towers at sunset with a construction crane"/>

    <!-- city photo area, right -->
    <polygon points="946,125 1200,125 1200,562 909,562" fill="url(#city-tones)"
             role="img" aria-label="Aerial photo of a downtown skyline with a tall tower and a stadium below"/>

    <!-- caption tag -->
    <polygon class="caption-tag" points="895,164 1125,164 1125,219 887,219" fill="var(--red)"/>
  </svg>

  <h1 class="title">LOREM IPSUM<br>DOLOR SIT</h1>

  <p class="headline">Lorem ipsum dolor<br>sit massa, adipiscing<br>consectetuer&nbsp; elit.</p>

  <p class="body-copy">
    <span class="line" style="left:539px; width:327px;">Lorem ipsum dolor sit amet,</span>
    <span class="line" style="left:536px; width:328px;">elit consectetuer adipiscing.</span>
    <span class="line" style="left:534px; width:328px;">Maecenas congue massa portti.</span>
    <span class="line" style="left:532px; width:327px;">Fusce sudet posuere, magna</span>
    <span class="line" style="left:529px; width:327px;">sed pulvinar. Purus et lectus</span>
    <span class="line last" style="left:527px;">malesuada libero urna.</span>
  </p>

  <div class="caption">CAPTION</div>

  <div class="brand">ORBIT</div>
</main>
</body>
</html>
```